Brightmeadow Equine Hemp horse feed supplement LABEL

Design a label for a horse feed supplement made from hemp. American grown hemp, American made product, American owned company. This is targeted towards the race horse market, so a race horse graphic would be ideal.

Our slogan "The cornerstone of equine wellness"

**When adding our logo, please change the lime green in our logo to #c1df7f **
Give TWO label options with the logo as described above and also an option with the word Equine removed from our logo.**

Target Market(s)

Performance Horses (Racing, team roping, cutting, reining, jumping)

Industry/Entity Type

Horseback Riding

Colors
eaf2ce
cadf82

Requirements
Must have
• - Brightmeadow Equine Logo AS DESCRIBED in project description
- Checkboxes at the bottom with different size package choice (1lb, 5lb, 10lb, 25lb, 50lb) - We will hand mark the size when packaging

The following benefits of CBD:
- Anti-Inflammatory
- Pain Relief
- Anti-Anxiety
- Acid Neutralizer

Dosing Instructions:
750mg - Gastric care, joint support, inflammation, arthritis, and stress (1/2 Scoop)
1500mg - Chronic pain, seizures, severe arthritis, and intense anxiety (Full scoop)

Ingredients: Cannabis Sativa (Hemp)
Nice to have
• Would like to be able to stick a QR code on the label that will change between batches of hemp.

```html
<!DOCTYPE html>
<html lang="en">
<head>
<meta charset="utf-8">
<title>Brightmeadow Equine Hemp – Label Options</title>
<link rel="stylesheet" href="https://fonts.googleapis.com/css2?family=Montserrat:wght@400;500;600;800&family=Nunito+Sans:wght@400;700&display=swap">
<style>
  :root{
    --sheet:#ffffff;
    --cream:#e3e2cc;
    --leaf-soft:#cadf82;
    --band-green:#80b541;
    --band-deep:#3d6a2f;
    --slogan:#c8e0a2;
    --logo-accent:#c1df7f;
    --ink-dark:#2f4a24;
    --yellow:#fff200;
    --white:#ffffff;
    --text:#333333;
    --grey:#8d8d8d;
    --horse:#9a4a22;
  }
  *{box-sizing:border-box;margin:0;padding:0}
  html,body{width:1130px;height:1200px;overflow:hidden;background:var(--sheet)}
  body{font-family:"Montserrat",sans-serif;color:var(--text)}
  .sheet{width:1300px;height:1385px;transform:scale(0.866);transform-origin:0 0;position:relative}
  .label{position:absolute;left:0;width:1300px;height:670px;background:var(--cream);overflow:hidden}
  .label--a{top:0}
  .label--b{top:710px}
  .leaf-pattern{position:absolute;inset:0;
    background:
      radial-gradient(ellipse 160px 120px at 1230px 40px, rgba(202,223,130,.75), transparent 70%),
      radial-gradient(ellipse 140px 90px at 850px 640px, rgba(202,223,130,.7), transparent 70%),
      radial-gradient(ellipse 120px 80px at 40px 40px, rgba(202,223,130,.6), transparent 70%),
      radial-gradient(ellipse 160px 110px at 1280px 560px, rgba(202,223,130,.7), transparent 70%),
      radial-gradient(ellipse 90px 70px at 600px 640px, rgba(202,223,130,.55), transparent 70%)}
  .hero{position:absolute;left:0;top:90px;width:830px;height:518px;background:var(--band-green)}
  .hero__lower{position:absolute;left:0;top:325px;width:100%;height:193px;
    background:linear-gradient(90deg,var(--band-deep) 0%,#4f8236 55%,#6ea43e 100%)}
  .slogan{position:absolute;left:0;top:276px;width:540px;height:49px;background:var(--slogan);
    font-weight:600;font-size:18px;letter-spacing:1px;color:#2c2c2c;display:flex;align-items:center;padding-left:54px;white-space:nowrap}
  .logo{position:absolute;left:190px;top:0;width:208px;height:172px;z-index:2}
  .logo svg{position:absolute;inset:0}
  .logo__name{position:absolute;left:0;right:0;top:66px;text-align:center;font-weight:500;font-size:21px;color:var(--grey)}
  .logo__dot{position:absolute;left:96px;top:38px;width:16px;height:16px;border-radius:50%;background:var(--logo-accent)}
  .title{position:absolute;left:155px;top:226px;font-weight:800;font-size:80px;letter-spacing:6px;color:var(--white);line-height:1}
  .subtitle{position:absolute;left:156px;top:303px;font-weight:600;font-size:22px;letter-spacing:.5px;color:var(--ink-dark)}
  .leaf-icon{position:absolute;left:440px;top:236px;width:78px;height:72px;border-radius:50% 50% 40% 40%;background:radial-gradient(circle,#1b1b1b 40%,rgba(27,27,27,0) 72%)}
  .label--b .leaf-icon{left:430px;top:254px}
  .horse{position:absolute;left:520px;top:100px;width:270px;height:500px;border-radius:45% 40% 20% 30%;
    background:radial-gradient(ellipse at 55% 40%,#b85a28 0%,var(--horse) 50%,rgba(120,55,25,0) 75%)}
  .benefits-head{position:absolute;left:98px;top:450px;width:391px;height:43px;background:var(--yellow);
    font-size:18px;letter-spacing:.3px;color:#222;display:flex;align-items:center;justify-content:center;white-space:nowrap}
  .benefits{position:absolute;left:98px;top:502px;width:391px;text-align:center;color:var(--white);font-size:20px;line-height:28px}
  .sizes{position:absolute;left:151px;top:598px}
  .size{position:absolute;top:0;width:36px;text-align:center;font-size:13px;color:#444}
  .size__box{display:block;width:36px;height:32px;background:var(--white);border:1px solid #8a8a8a;border-radius:7px;margin-bottom:5px}
  .info{position:absolute;left:846px;top:88px;width:407px;height:515px;background:var(--white);border-radius:22px}
  .dosing{position:absolute;left:15px;top:19px;width:376px;height:181px;border:1.5px solid #555;border-radius:12px;padding:20px 0 0 21px}
  .heading{font-size:20px;font-weight:500;color:#222;display:inline-block;padding:0 26px 2px 0;border-bottom:4px solid #333}
  .dose{font-family:"Nunito Sans",sans-serif;font-size:15.5px;line-height:21px;margin-top:16px;color:#333;white-space:nowrap}
  .dose b{font-weight:700}
  .ingredients{position:absolute;left:31px;top:214px}
  .ingredients .heading{padding-right:28px}
  .ingredients p{font-family:"Nunito Sans",sans-serif;font-size:16px;margin-top:10px}
  .divider{position:absolute;left:31px;top:304px;width:206px;border-top:2.5px solid #333}
  .company{position:absolute;left:25px;top:324px;font-size:15px}
  .qr-area{position:absolute;left:255px;top:235px;width:137px;height:257px;border:1.5px solid #555}
</style>
</head>
<body>
<main class="sheet">

  <section class="label label--a" aria-label="Label option with full name">
    <div class="leaf-pattern" role="img" aria-label="Faint hemp leaf background pattern"></div>
    <div class="hero">
      <div class="hero__lower"></div>
      <div class="slogan">THE CORNERSTONE OF EQUINE WELLNESS</div>
    </div>
    <div class="logo">
      <svg viewBox="0 0 208 172" width="208" height="172"><polygon points="0,0 208,0 208,152 104,172 0,152" fill="#fff" stroke="#cfcfcf"/></svg>
      <span class="logo__dot"></span>
      <div class="logo__name">Brightmeadow Equine</div>
    </div>
    <h1 class="title">HEMP</h1>
    <div class="leaf-icon" role="img" aria-label="Hemp leaf icon"></div>
    <p class="subtitle">HORSE SUPPLEMENT</p>
    <div class="horse" role="img" aria-label="Photo of a bay race horse cantering"></div>
    <div class="benefits-head">THE FOLLOWING BENEFITS OF CBD:</div>
    <p class="benefits">Anti-Inflammatory | Pain Relief<br>Anti-Anxiety | Acid Neutralizer</p>
    <div class="sizes">
      <span class="size" style="left:0"><i class="size__box"></i>1lb</span>
      <span class="size" style="left:65px"><i class="size__box"></i>5lb</span>
      <span class="size" style="left:127px"><i class="size__box"></i>10lb</span>
      <span class="size" style="left:192px"><i class="size__box"></i>25lb</span>
      <span class="size" style="left:249px"><i class="size__box"></i>50lb</span>
    </div>
    <div class="info">
      <div class="dosing">
        <h2 class="heading">DOSING INSTRUCTIONS</h2>
        <p class="dose"><b>750mg</b> – Gastric care, joint support,<br>inflammation, arthritis, and stress (1/2 Scoop)</p>
        <p class="dose"><b>1500mg</b> – Chronic pain, seizures, severe<br>arthritis, and intense anxiety (Full scoop)</p>
      </div>
      <div class="ingredients">
        <h2 class="heading">INGREDIENTS</h2>
        <p>Cannabis Sativa (Hemp)</p>
      </div>
      <div class="divider"></div>
      <p class="company">COMPANY DETAILS</p>
      <div class="qr-area"></div>
    </div>
  </section>

  <section class="label label--b" aria-label="Label option with short name">
    <div class="leaf-pattern" role="img" aria-label="Faint hemp leaf background pattern"></div>
    <div class="hero">
      <div class="hero__lower"></div>
      <div class="slogan">THE CORNERSTONE OF EQUINE WELLNESS</div>
    </div>
    <div class="logo">
      <svg viewBox="0 0 208 172" width="208" height="172"><polygon points="0,0 208,0 208,152 104,172 0,152" fill="#fff" stroke="#cfcfcf"/></svg>
      <span class="logo__dot"></span>
      <div class="logo__name">Brightmeadow</div>
    </div>
    <h1 class="title">HEMP</h1>
    <div class="leaf-icon" role="img" aria-label="Hemp leaf icon"></div>
    <p class="subtitle">HORSE SUPPLEMENT</p>
    <div class="horse" role="img" aria-label="Photo of a bay race horse cantering"></div>
    <div class="benefits-head">THE FOLLOWING BENEFITS OF CBD:</div>
    <p class="benefits">Anti-Inflammatory | Pain Relief<br>Anti-Anxiety | Acid Neutralizer</p>
    <div class="sizes">
      <span class="size" style="left:0"><i class="size__box"></i>1lb</span>
      <span class="size" style="left:65px"><i class="size__box"></i>5lb</span>
      <span class="size" style="left:127px"><i class="size__box"></i>10lb</span>
      <span class="size" style="left:192px"><i class="size__box"></i>25lb</span>
      <span class="size" style="left:249px"><i class="size__box"></i>50lb</span>
    </div>
    <div class="info">
      <div class="dosing">
        <h2 class="heading">DOSING INSTRUCTIONS</h2>
        <p class="dose"><b>750mg</b> – Gastric care, joint support,<br>inflammation, arthritis, and stress (1/2 Scoop)</p>
        <p class="dose"><b>1500mg</b> – Chronic pain, seizures, severe<br>arthritis, and intense anxiety (Full scoop)</p>
      </div>
      <div class="ingredients">
        <h2 class="heading">INGREDIENTS</h2>
        <p>Cannabis Sativa (Hemp)</p>
      </div>
      <div class="divider"></div>
      <p class="company">COMPANY DETAILS</p>
      <div class="qr-area"></div>
    </div>
  </section>

</main>
</body>
</html>
```